Photography Studio Website (Design Only)

*Profile:
Omar Tenzali Studios is a boutique photography and art studio, and specialize in mixed media and digital arts. We offer a personalized and distinct portraiture photographic experience that does not only capture the natural magic of our clients' personality, but also spices it up with our own creative sauce to turn their images into timeless work of art that they can be proud to show off.
In addition to Portrait Photography, our studio also caters for art lovers who are passionate about decorating their space with unique pieces of art, we offer a huge collection of photographic and digitally painted artwork from our own art line collection.
Clients looking for the ultimate portraiture or fine art experience will be treated to a larger than life custom-designed artwork for them to share and enjoy for lifetime.
*What we need:
We need to design a cohesive website (Portfolio+Blog) that reflects the nature of our high-quality artwork and professional portrait photography service level specially in Glamour and Conceptual portraits. Also Since we also sell art prints in addition to portrait work we need the website to reflect that sense of high-end art gallery.
*The Design Aesthetics:
- Sophisticated
- Clean
- Artistic
- User Friendly (Easy/simple to navigate)
- The main focus of website is the images
*Content:
-Menu:
Home | Passion & Vision | Experiences | Portfolios | Connect | Testimonials | Blog | The Store
- Home Page:
Slideshow (with headlines)
Under the Slideshow we need to have 4 blocks that feature our main categories of specialty:
1-Glamour Portraits
2- Conceptual Portraits
3- Travel Art Photography
4- Fine Arts Photography
The blocks will show the latests blog posts in each respective category (5 lines under each block: post title only)- something similar to this: http://dravenholt.com
- Search box
- Social Media Icons: Facebook | Twitter | Pinterest| Instagram | YouTube
- Information & News Updates E-mail Subscription box
- Brand Colors: Attached PDF has the logo & Colors in Vector (Please stick to brand colors only)
- Brand Fonts:
JosefinSansStd-Light
You can check the current design on the following link:
Www.omartenzalistudios.com
Target Market(s)
Main Target: Women (25-40 yrs) | Secondary Targets: Artists & Musicians | Art Collectors
Industry/Entity Type
Portrait Photography
Look and feel

```html
<!DOCTYPE html>
<html lang="en">
<head>
<meta charset="utf-8">
<title>Omar Tenzali Studios</title>
<link href="https://fonts.googleapis.com/css2?family=Josefin+Sans:wght@300;400&display=swap" rel="stylesheet">
<style>
  :root {
    --ink: #3b3b3b;
    --gold: #d8cc98;
    --peach: #e8b58c;
    --rose: #d5abbf;
    --sky: #8ea4c5;
    --sage: #b8c98d;
    --paper: #ffffff;
    --band: rgba(255, 255, 255, 0.55);
  }
  * { margin: 0; padding: 0; box-sizing: border-box; }
  html, body { width: 960px; height: 1200px; overflow: hidden; }
  body {
    position: relative;
    background: var(--paper);
    font-family: "Josefin Sans", sans-serif;
    font-weight: 300;
    color: var(--ink);
  }
  .social { position: absolute; top: 13px; right: 11px; display: flex; gap: 6px; }
  .social-dot { width: 26px; height: 26px; border-radius: 50%; background: #2e2e2e; }

  .brand-mark { position: absolute; top: 64px; left: 467px; width: 26px; height: 26px; background: var(--gold); }
  .brand-name {
    position: absolute; top: 145px; left: 0; width: 960px; text-align: center;
    font-size: 28px; line-height: 31px; font-weight: 400; color: var(--ink);
  }

  .main-nav {
    position: absolute; top: 242px; left: 36px; width: 888px; height: 28px;
    display: flex; justify-content: space-between; align-items: center;
    font-size: 24px; line-height: 28px; list-style: none; white-space: nowrap;
  }
  .nav-sep { width: 1px; height: 24px; background: var(--gold); }

  .hero {
    position: absolute; top: 282px; left: 0; width: 960px; height: 477px;
    background:
      radial-gradient(ellipse 120px 80px at 480px 230px, rgba(230,225,215,0.55), transparent 70%),
      linear-gradient(175deg, transparent 55%, rgba(200,195,185,0.35) 70%, transparent 85%),
      linear-gradient(180deg, #101010 0%, #2a2a28 40%, #6b6862 62%, #3a3936 80%, #4e4c48 100%);
  }
  .hero-caption { position: absolute; right: 0; bottom: 4px; width: 515px; height: 33px; background: var(--band); }
  .hero-caption svg { display: block; overflow: visible; }
  .hero-caption text { font-family: "Josefin Sans", sans-serif; font-weight: 300; font-size: 42px; fill: #2c2c2c; }

  .categories { position: absolute; top: 798px; left: 0; width: 960px; display: flex; }
  .category { width: 240px; text-align: center; }
  .category-mark { width: 40px; height: 40px; margin: 17px auto 0; }
  .category-title { font-size: 21px; line-height: 30px; font-weight: 400; margin: 23px 0 5px; white-space: nowrap; }
  .post-list { list-style: none; display: inline-block; text-align: left; font-size: 19px; }
  .post-list li { height: 26.6px; display: flex; align-items: center; gap: 6px; }
  .bullet { width: 7px; height: 7px; transform: rotate(45deg); margin-right: 2px; }
  .glamour .category-mark, .glamour .bullet { background: var(--peach); }
  .conceptual .category-mark, .conceptual .bullet { background: var(--rose); }
  .travel .category-mark, .travel .bullet { background: var(--sky); }
  .fine-arts .category-mark, .fine-arts .bullet { background: var(--sage); }

  .site-footer { position: absolute; top: 1109px; left: 0; width: 960px; height: 91px; background: var(--gold); }
  .footer-links { position: absolute; top: 27px; left: 0; width: 960px; text-align: center; font-size: 18px; }
  .copyright { position: absolute; left: 21px; bottom: 9px; font-size: 12px; }
</style>
</head>
<body>
  <div class="social" aria-label="Social links">
    <span class="social-dot"></span><span class="social-dot"></span>
    <span class="social-dot"></span><span class="social-dot"></span>
  </div>

  <div class="brand-mark"></div>
  <div class="brand-name">OMAR TENZALI<br>STUDIOS</div>

  <ul class="main-nav">
    <li>home</li><li class="nav-sep"></li>
    <li>passion &amp; vision</li><li class="nav-sep"></li>
    <li>experiences</li><li class="nav-sep"></li>
    <li>portfolios</li><li class="nav-sep"></li>
    <li>connect</li><li class="nav-sep"></li>
    <li>testimonials</li><li class="nav-sep"></li>
    <li>blog</li><li class="nav-sep"></li>
    <li>the store</li>
  </ul>

  <section class="hero" role="img" aria-label="Black and white night photograph of a Paris avenue with light trails leading to a triumphal arch">
    <div class="hero-caption">
      <svg width="515" height="33" viewBox="0 0 515 33">
        <text x="2" y="32" textLength="510" lengthAdjust="spacingAndGlyphs">FEATURED WORK // PARIS</text>
      </svg>
    </div>
  </section>

  <section class="categories">
    <div class="category glamour">
      <div class="category-mark"></div>
      <h2 class="category-title">glamour portraits</h2>
      <ul class="post-list">
        <li><span class="bullet"></span>lorum ipsum</li><li><span class="bullet"></span>lorum ipsum</li>
        <li><span class="bullet"></span>lorum ipsum</li><li><span class="bullet"></span>lorum ipsum</li>
        <li><span class="bullet"></span>lorum ipsum</li>
      </ul>
    </div>
    <div class="category conceptual">
      <div class="category-mark"></div>
      <h2 class="category-title">conceptual portraits</h2>
      <ul class="post-list">
        <li><span class="bullet"></span>lorum ipsum</li><li><span class="bullet"></span>lorum ipsum</li>
        <li><span class="bullet"></span>lorum ipsum</li><li><span class="bullet"></span>lorum ipsum</li>
        <li><span class="bullet"></span>lorum ipsum</li>
      </ul>
    </div>
    <div class="category travel">
      <div class="category-mark"></div>
      <h2 class="category-title">travel art photography</h2>
      <ul class="post-list">
        <li><span class="bullet"></span>lorum ipsum</li><li><span class="bullet"></span>lorum ipsum</li>
        <li><span class="bullet"></span>lorum ipsum</li><li><span class="bullet"></span>lorum ipsum</li>
        <li><span class="bullet"></span>lorum ipsum</li>
      </ul>
    </div>
    <div class="category fine-arts">
      <div class="category-mark"></div>
      <h2 class="category-title">fine arts photography</h2>
      <ul class="post-list">
        <li><span class="bullet"></span>lorum ipsum</li><li><span class="bullet"></span>lorum ipsum</li>
        <li><span class="bullet"></span>lorum ipsum</li><li><span class="bullet"></span>lorum ipsum</li>
        <li><span class="bullet"></span>lorum ipsum</li>
      </ul>
    </div>
  </section>

  <footer class="site-footer">
    <nav class="footer-links">terms &amp; conditions | privacy policy | faqs | delivery info | contact us |</nav>
    <p class="copyright">© 2013 Omar Tenzali Studios.</p>
  </footer>
</body>
</html>
```